TK Drafting

Simple Design - Logo is done (from this site). Logo on one side - Back Side an image or outline of a house blue print - My name, phone, email, website url. Prefer the traditional Architectural style of letters -

Target Market(s)

Customers who need a floor plan redesigned for renovations or realtors who want a floor plan for marketing their listings

Industry/Entity Type

Architecture

Contact Information for Business Card

Colin Varga - Name
318-542-6604 - Phone
tkdraftingco@mailvane.com
www.tkdraftingco.net

Font styles to use
Other font styles liked:
• Architecture writing -

Colors
0555a3
3276b5
85acd3

Requirements
Must have
• Logo that is attached. I like an indigo blue color for the background or a royal blue - gray logo OR - white and clean with the logo on one side and the same color gray lettering on the other side
Nice to have
• some sort of image that shows a residential blue print. It may not be possible on this small of a card though.
Should not have
• Nothing cartoonish.

```html
<!DOCTYPE html>
<html lang="en">
<head>
<meta charset="utf-8">
<title>TK Drafting — Business Card</title>
<link href="https://fonts.googleapis.com/css2?family=Aldrich&family=Roboto+Condensed:wght@300;400&display=swap" rel="stylesheet">
<style>
  :root {
    --backdrop: #e6e6e6;
    --royal-blue: #00378c;
    --card-white: #ffffff;
    --mark-gray: #b1b2b7;
    --text-gray: #a8a9ae;
    --rule-gray: #e3e3e6;
    --ghost-gray: #ececee;
  }
  * { margin: 0; padding: 0; box-sizing: border-box; }
  html, body {
    width: 1200px;
    height: 707px;
    overflow: hidden;
    background: var(--backdrop);
  }
  .sheet {
    position: relative;
    width: 1200px;
    height: 707px;
  }
  .card {
    position: absolute;
    top: 201px;
    width: 387px;
    height: 242px;
    overflow: hidden;
    box-shadow: 0 1px 3px rgba(0, 0, 0, 0.18);
  }
  .card--front {
    left: 176px;
    background: var(--royal-blue);
    display: flex;
    align-items: center;
    justify-content: center;
  }
  .card--back {
    left: 633px;
    background: var(--card-white);
  }
  .wordmark {
    display: flex;
    align-items: center;
    gap: 10px;
    color: var(--mark-gray);
    font-family: "Aldrich", sans-serif;
    font-size: 26px;
    letter-spacing: 2px;
    text-transform: uppercase;
  }
  .wordmark__square {
    width: 18px;
    height: 18px;
    background: var(--mark-gray);
  }
  .contact {
    position: absolute;
    left: 46px;
    top: 80px;
    color: var(--text-gray);
  }
  .contact__name {
    font-family: "Aldrich", sans-serif;
    font-size: 19px;
    line-height: 1;
    font-weight: 400;
    letter-spacing: 0.5px;
    text-transform: uppercase;
    white-space: nowrap;
  }
  .contact__rule {
    width: 136px;
    height: 1px;
    margin: 16px 0 14px 1px;
    background: var(--rule-gray);
    border: 0;
  }
  .contact__phone {
    font-family: "Roboto Condensed", sans-serif;
    font-weight: 300;
    font-size: 19px;
    line-height: 1;
    letter-spacing: 0.3px;
    margin-bottom: 14px;
  }
  .contact__line {
    font-family: "Roboto Condensed", sans-serif;
    font-weight: 300;
    font-size: 11.5px;
    line-height: 19px;
  }
  .ghost-square {
    position: absolute;
    right: -40px;
    bottom: -40px;
    width: 170px;
    height: 170px;
    background: var(--ghost-gray);
  }
</style>
</head>
<body>
  <main class="sheet">
    <section class="card card--front" aria-label="Card front">
      <div class="wordmark">
        <span class="wordmark__square" aria-hidden="true"></span>
        <span class="wordmark__name">TK Drafting</span>
      </div>
    </section>

    <section class="card card--back" aria-label="Card back">
      <div class="ghost-square" aria-hidden="true"></div>
      <div class="contact">
        <h1 class="contact__name">Colin Varga</h1>
        <hr class="contact__rule">
        <p class="contact__phone">318-542-6604</p>
        <p class="contact__line">tkdraftingco@mailvane.com</p>
        <p class="contact__line">www.tkdraftingco.net</p>
      </div>
    </section>
  </main>
</body>
</html>
```